Geschäftspapiere für Unternehmensberatung
Zielgruppe
Wir machen Unternehmensberatung, Prozessoptimierung, Change Management,
Buchhaltung.
Unsere Zielgruppe sind Firmen, denen es wirtschaftlich nicht so gut geht und die Hilfe benötigen.
Aufgabenstellung
Wir möchten ein CI an unser Logo angepasst.
Es darf gerne etwas besonderes sein.

```html
<!DOCTYPE html>
<html lang="de">
<head>
<meta charset="utf-8">
<title>Kaeder Consulting – Geschäftspapiere</title>
<link href="https://fonts.googleapis.com/css2?family=Open+Sans:wght@400;600;700&display=swap" rel="stylesheet">
<style>
  :root{
    --bg:#e4e4e8;
    --paper:#f4f5f8;
    --ink:#262628;
    --ink-soft:#3a3a3d;
    --blue:#1f4f9a;
    --grey:#8a8f99;
    --faint:#dfe1e8;
    --faint-dark:#2e2f33;
  }
  *{margin:0;padding:0;box-sizing:border-box}
  html,body{width:1200px;height:798px;overflow:hidden;background:var(--bg);font-family:"Open Sans",sans-serif;color:var(--ink)}
  .canvas{position:relative;width:1200px;height:798px}
  .piece{position:absolute;overflow:hidden;box-shadow:0 6px 18px rgba(0,0,0,.18)}
  .brand{display:flex;align-items:center;gap:5px;font-weight:600;letter-spacing:.08em;text-transform:uppercase;color:var(--grey);white-space:nowrap}
  .brand-dot{border-radius:50%;border:1.5px solid var(--grey);flex:none}
  .corner{position:absolute;top:0;right:0}
  .watermark{position:absolute;border-radius:50%;background:var(--faint)}

  /* business cards */
  .card{width:190px;height:104px;border-radius:6px;background:var(--ink)}
  .card--front{left:70px;top:72px;display:flex;align-items:center;justify-content:center}
  .card--front .brand{font-size:11px}
  .card--front .brand-dot{width:12px;height:12px}
  .card--back{left:110px;top:190px;padding:14px}
  .card--back .brand{font-size:7px}
  .card--back .brand-dot{width:8px;height:8px}
  .card-name{position:absolute;left:70px;top:22px;color:#e8e8ec;font-size:8px;font-weight:700;letter-spacing:.05em}
  .card-role{position:absolute;left:70px;top:33px;color:var(--grey);font-size:6px}
  .card-contact{position:absolute;left:70px;top:48px;color:#c7c9d0;font-size:5.5px;line-height:1.6}

  /* letterhead */
  .letter{left:366px;top:102px;width:300px;height:423px;background:var(--paper)}
  .letter .watermark{left:24px;top:72px;width:250px;height:250px;opacity:.7}
  .letter .brand{position:absolute;left:25px;top:50px;font-size:11px}
  .letter .brand-dot{width:15px;height:15px}
  .letter-date{position:absolute;left:95px;top:109px;font-size:6.2px;letter-spacing:.05em}
  .sender{position:absolute;left:21px;top:147px}
  .sender-name{font-size:7.4px;font-weight:700}
  .sender-role{font-size:6px;color:var(--grey);letter-spacing:.05em;margin-top:2px}
  .letter-body{position:absolute;left:95px;top:147px;width:171px;font-size:6.1px;line-height:1.25;text-align:justify;letter-spacing:.03em}
  .letter-body p+p{margin-top:7px}
  .letter-body .subject{font-size:6.8px}
  .signature{position:absolute;right:34px;top:305px;font-size:7px;font-weight:700}
  .company{position:absolute;left:18px;top:328px;font-size:4.6px;line-height:1.5;font-weight:600}
  .company-name{font-size:11px;font-weight:700;letter-spacing:-.02em;margin-bottom:4px}
  .company hr{border:0;border-top:1px solid var(--ink);width:58px;margin:2px 0}
  .letter-foot{position:absolute;left:95px;top:398px;width:176px;border-top:1px solid var(--ink);padding-top:7px;font-size:4.4px;font-weight:600;white-space:nowrap}

  /* compliment slip */
  .slip{left:714px;top:72px;width:336px;height:168px;background:var(--paper)}
  .slip .watermark{left:168px;top:12px;width:138px;height:138px}
  .slip .brand{position:absolute;left:29px;top:35px;font-size:8px}
  .slip .brand-dot{width:12px;height:12px}
  .slip-contact{position:absolute;left:31px;top:102px;font-size:4.6px;font-weight:600;line-height:1.55}
  .slip-contact hr{border:0;border-top:1px solid var(--ink);width:66px;margin:3px 0}

  /* folder */
  .folder{left:718px;top:255px;width:333px;height:445px;background:var(--ink)}
  .folder .watermark{left:34px;top:93px;width:250px;height:250px;background:var(--faint-dark)}
  .folder .brand{position:absolute;right:34px;top:392px;font-size:10.5px;letter-spacing:.05em}
  .folder .brand-dot{width:16px;height:16px}

  /* envelope */
  .envelope{left:332px;top:552px;width:332px;height:168px;background:var(--paper)}
  .flap{position:absolute;left:4px;top:0;width:324px;height:44px;background:var(--ink);border-radius:0 0 10px 10px}
  .envelope .brand{position:absolute;left:50%;top:17px;transform:translateX(-50%);font-size:7px}
  .envelope .brand-dot{width:10px;height:10px}
</style>
</head>
<body>
<main class="canvas">

  <section class="piece card card--front" aria-label="Visitenkarte Vorderseite">
    <div class="brand"><span class="brand-dot"></span>Kaeder Consulting</div>
  </section>

  <section class="piece card card--back" aria-label="Visitenkarte Rückseite">
    <div class="brand"><span class="brand-dot"></span>Kaeder</div>
    <div class="card-name">JONAS WELLER</div>
    <div class="card-role">Berater</div>
    <div class="card-contact">040 123 4567<br>jw@kaeder.de<br>www.kaeder.de<br>Kaistraße 12 Hamburg</div>
  </section>

  <section class="piece letter" aria-label="Briefbogen">
    <div class="watermark"></div>
    <svg class="corner" width="34" height="50" viewBox="0 0 34 50"><path d="M0 0H34V50L0 30Z" fill="var(--ink)"/></svg>
    <div class="brand"><span class="brand-dot"></span>Kaeder Consulting</div>
    <div class="letter-date">Sep 27, 2019</div>
    <div class="sender">
      <div class="sender-name">SELMA ROTH</div>
      <div class="sender-role">Directrice</div>
    </div>
    <div class="letter-body">
      <p><span class="subject">Sep 27, 2019 (LMR Market</span><br>Intelligence via NEWSLINE) -- A new market study on Global Pet Medicine Market with 100+ market data Tables, Pie Chart &amp; Graphs is released that will provide complete assessment of the Market and covers evolving trends, current scenario analysis and growth factors, and industry validated market data. The research study provides market breakdown by re</p>
      <p>venue and volume (if applicable) and price history estimates for Global Pet Medicine. Some are the key players from the coverage that are also part of the study are Pellham Vet, Zorvan, Marlow, Elvora, Baxen, Virlo, Cerva Animale, Vetonix, Brema Animal Health &amp; Dekta Pharmaceuticals.<br>Get ready to identify the pros and cons of regulatory framework of the Indus</p>
    </div>
    <div class="signature">SIGNATURE</div>
    <div class="company">
      <div class="company-name">Hafenrat</div>
      RC: 1655<br>patente: 45409285<br>I.F : 20787472
      <hr>
      CNSS: 9241431<br>ICE: 001884885000028
    </div>
    <div class="letter-foot">TEL: 0401234567 - info@kaeder-beratung.de - web : www.kaeder-beratung.de - 12</div>
  </section>

  <section class="piece slip" aria-label="Kurzmitteilung">
    <div class="watermark"></div>
    <svg class="corner" width="22" height="50" viewBox="0 0 22 50"><path d="M0 0H22V50L0 30Z" fill="var(--ink)"/></svg>
    <div class="brand"><span class="brand-dot"></span>Kaeder Consulting</div>
    <div class="slip-contact">
      TEL: 0401234567<br>mail: info@kaeder-beratung.de<br>WEB: www.kaeder-beratung.de
      <hr>
      Kaistraße 12 | 20457<br>Hamburg
    </div>
  </section>

  <section class="piece folder" aria-label="Präsentationsmappe">
    <div class="watermark"></div>
    <svg class="corner" width="22" height="50" viewBox="0 0 22 50"><path d="M0 0H22V50L0 30Z" fill="var(--paper)"/></svg>
    <div class="brand"><span class="brand-dot"></span>Kaeder Consulting</div>
  </section>

  <section class="piece envelope" aria-label="Briefumschlag">
    <div class="flap"></div>
    <div class="brand"><span class="brand-dot"></span>Kaeder Consulting</div>
  </section>

</main>
</body>
</html>
```